Chewable Dog Supplements jar with lid

Below are some specifications of this project: 
There will be 6 different types of dog supplements in different jars, which will have different colors, or elements(dogs),  but will respect the same theme overall.  I attached some pictures below as a reference.
 The design I would like to create is for a label that will go around and on the top of a round plastic jar. The size of the product label is 25cm long and 8.5 cm high and on the top there is a circle that goes on the lid with the exact same design as on the front.
Some small pictures on the back with no Grain, Corn or Soy derivates  
 All products come in different shapes chews 
All products have 3 different headlines with their benefits that go on the front of the design.
All products have different flavors.
Regarding the text that will go on the back of the product, I can help with adding that to all products as long as we agree on how it looks. On the back I will need a space for a barcode, best before date, there should be 2 tables with ingredients and directions for use, and space for text under :Storage instructions, Warning, Description.

Target Market(s)

Europe

Industry/Entity Type

pet food

Requirements
Must have
• Trust signals ( Free from GMO, Natural ingredients, Free from artificial colouring) and a text box with the benefits of the product that I will provide.

```html
<!DOCTYPE html>
<html lang="en">
<head>
<meta charset="utf-8">
<title>Chewable Dog Supplement Labels</title>
<link href="https://fonts.googleapis.com/css2?family=Fredoka:wght@500;600;700&family=Montserrat:wght@600&display=swap" rel="stylesheet">
<style>
  :root {
    --backdrop: #414141;
    --paper: #ececef;
    --ink: #333333;
    --sun: #f6c544;
    --no-red: #e8533a;
    --blue: #3a52a8;
    --orange: #f08a2b;
    --teal: #3dbfad;
  }
  * { margin: 0; padding: 0; box-sizing: border-box; }
  html, body { width: 1200px; height: 981px; overflow: hidden; background: var(--backdrop); }
  .canvas { position: relative; width: 1200px; height: 981px; }

  .wrap-label {
    position: absolute; left: 64px; width: 770px; height: 261px;
    background: var(--paper);
    box-shadow: 0 2px 6px rgba(0,0,0,.35);
  }
  .label-hip { top: 55px; --accent: var(--blue); }
  .label-skin { top: 359px; --accent: var(--orange); }
  .label-multi { top: 684px; --accent: var(--teal); }

  .brand-name {
    position: absolute; left: 48px; top: 168px; width: 140px; text-align: center;
    font-family: "Montserrat", sans-serif; font-weight: 600; font-size: 17px;
    letter-spacing: 4px; color: var(--ink);
  }
  .product-title {
    position: absolute; left: 211px; top: 38px;
    font-family: "Fredoka", sans-serif; font-weight: 700; font-size: 40px;
    color: var(--accent); line-height: 1; white-space: nowrap;
  }
  .mascot-art {
    position: absolute; left: 226px; top: 96px; width: 161px; height: 111px;
    border-radius: 40px 50px 30px 30px;
    background: radial-gradient(circle at 55% 45%, var(--sun) 60%, rgba(246,197,68,.2) 100%);
  }
  .free-from-badge {
    position: absolute; left: 516px; top: 54px; width: 76px; height: 76px;
    border-radius: 50%; background: var(--accent);
    display: flex; flex-direction: column; align-items: center; justify-content: center;
    font-family: "Fredoka", sans-serif; font-weight: 600; text-align: center; line-height: 1.05;
  }
  .free-from-badge .no { color: var(--no-red); font-size: 16px; font-weight: 700; }
  .free-from-badge .items { color: #fff; font-size: 9.5px; }
  .free-from-badge .derivates { color: var(--sun); font-size: 9.5px; }

  .benefit-list { position: absolute; left: 458px; top: 146px; list-style: none; }
  .benefit-list li {
    position: relative; padding-left: 30px; margin-bottom: 10px;
    font-family: "Fredoka", sans-serif; font-weight: 600; font-size: 14px;
    line-height: 15px; color: var(--sun);
  }
  .benefit-list li::before {
    content: ""; position: absolute; left: 4px; top: 1px; width: 14px; height: 14px;
    border-radius: 50%; background: var(--accent);
  }

  .lid-label {
    position: absolute; left: 888px; width: 246px; height: 246px; border-radius: 50%;
    background: var(--paper); border: 9px solid var(--accent);
    box-shadow: 0 0 0 2px #f4f4f6, 0 2px 6px rgba(0,0,0,.35);
  }
  .lid-hip { top: 63px; --accent: var(--blue); }
  .lid-skin { top: 367px; --accent: var(--orange); }
  .lid-multi { top: 692px; --accent: var(--teal); }
  .lid-label .lid-brand {
    position: absolute; top: 44px; width: 100%; text-align: center;
    font-family: "Montserrat", sans-serif; font-weight: 600; font-size: 6px;
    letter-spacing: 1.5px; color: var(--ink);
  }
  .lid-label .lid-title {
    position: absolute; top: 62px; width: 100%; text-align: center;
    font-family: "Fredoka", sans-serif; font-weight: 700; font-size: 29px;
    color: var(--accent); line-height: 1;
  }
  .lid-label .lid-mascot {
    position: absolute; left: 45px; top: 108px; width: 130px; height: 96px;
    border-radius: 34px 40px 26px 26px;
    background: radial-gradient(circle at 55% 45%, var(--sun) 60%, rgba(246,197,68,.2) 100%);
  }
</style>
</head>
<body>
<main class="canvas">

  <section class="wrap-label label-hip">
    <div class="brand-name">NUTRIPAW</div>
    <h2 class="product-title">HIP &amp; JOINT</h2>
    <div class="mascot-art" role="img" aria-label="Illustration of a happy yellow dog trotting, with blue ear and tail accents"></div>
    <div class="free-from-badge"><span class="no">NO</span><span class="items">GRAIN, CORN,<br>or SOY</span><span class="derivates">derivates</span></div>
    <ul class="benefit-list">
      <li>Walk and play with ease</li>
      <li>Fight inflammation<br>&amp; joint swelling</li>
      <li>Protect against wear</li>
    </ul>
  </section>

  <section class="wrap-label label-skin">
    <div class="brand-name">NUTRIPAW</div>
    <h2 class="product-title">SKIN &amp; COAT</h2>
    <div class="mascot-art" role="img" aria-label="Illustration of a happy yellow dog trotting, with orange ear and tail accents"></div>
    <div class="free-from-badge"><span class="no">NO</span><span class="items">GRAIN, CORN,<br>or SOY</span><span class="derivates">derivates</span></div>
    <ul class="benefit-list">
      <li>Walk and play with ease</li>
      <li>Fight inflammation<br>&amp; joint swelling</li>
      <li>Protect against wear</li>
    </ul>
  </section>

  <section class="wrap-label label-multi">
    <div class="brand-name">NUTRIPAW</div>
    <h2 class="product-title" style="left:219px">MULTIVITA</h2>
    <div class="mascot-art" role="img" aria-label="Illustration of a happy yellow dog trotting, with teal ear and tail accents"></div>
    <div class="free-from-badge"><span class="no">NO</span><span class="items">GRAIN, CORN,<br>or SOY</span><span class="derivates">derivates</span></div>
    <ul class="benefit-list">
      <li>Walk and play with ease</li>
      <li>Fight inflammation<br>&amp; joint swelling</li>
      <li>Protect against wear</li>
    </ul>
  </section>

  <section class="lid-label lid-hip">
    <div class="lid-brand">NUTRIPAW</div>
    <h3 class="lid-title">HIP &amp; JOINT</h3>
    <div class="lid-mascot" role="img" aria-label="Illustration of a happy yellow dog trotting, with blue accents"></div>
  </section>

  <section class="lid-label lid-skin">
    <div class="lid-brand">NUTRIPAW</div>
    <h3 class="lid-title">SKIN &amp; COAT</h3>
    <div class="lid-mascot" role="img" aria-label="Illustration of a happy yellow dog trotting, with orange accents"></div>
  </section>

  <section class="lid-label lid-multi">
    <div class="lid-brand">NUTRIPAW</div>
    <h3 class="lid-title">MULTIVITA</h3>
    <div class="lid-mascot" role="img" aria-label="Illustration of a happy yellow dog trotting, with teal accents"></div>
  </section>

</main>
</body>
</html>
```